Bluefern Roving Sonography
Business Cards & Stationary
Bluefern Roving Sonography - Imaging
Creative Brief
Professional
Dana Whitlock
President
4072 Heron Crest Blvd #218 Royal Palm Beach, Florida 33411
bluefern.roving.bs@kelvamail.net
bluefernrovingsonography.com
Abdomen (AB) Vascular Technology (VT) Obstetrics and Gynecology (OB/GYN) Breast (BR) Pediatric Sonography (PS) Fetal Echocardiography (FE) Adult Echocardiography (AE) Pediatric Echocardiography (PE) Musculoskeletal Sonography (MSK)
Concepts
Logo for mobile ultrasound
dwhitlock482 dwhitlock482
I need to add health screenings to the back of the card

```html
<!DOCTYPE html>
<html lang="en">
<head>
<meta charset="utf-8">
<title>Bluefern Roving Sonography – Business Card</title>
<link rel="stylesheet" href="https://fonts.googleapis.com/css2?family=Open+Sans:ital,wght@0,400;0,600;0,700;1,600;1,700&display=swap">
<style>
  :root {
    --page-bg: #e9eaec;
    --card-bg: #ffffff;
    --brand-blue: #1d7fae;
    --deep-blue: #0f5f88;
    --light-blue: #2fa6d6;
    --band-grey: #4f5154;
    --text-grey: #5a5c5f;
    --on-blue: #ffffff;
  }
  * { box-sizing: border-box; margin: 0; padding: 0; }
  html, body { width: 1200px; height: 900px; overflow: hidden; }
  body {
    background: var(--page-bg);
    font-family: "Open Sans", Arial, sans-serif;
    position: relative;
  }
  .card {
    position: absolute;
    left: 285px;
    width: 630px;
    height: 360px;
    background: var(--card-bg);
    border-radius: 22px;
    overflow: hidden;
    box-shadow: 0 6px 18px rgba(0,0,0,0.18);
  }
  .card--back { top: 50px; }
  .card--front { top: 490px; }

  .brand {
    display: flex;
    align-items: center;
    gap: 12px;
    color: var(--brand-blue);
    font-weight: 700;
    font-size: 24px;
    letter-spacing: 0.2px;
  }
  .brand__dot {
    width: 34px; height: 34px;
    border-radius: 50%;
    background: var(--brand-blue);
    flex: none;
  }
  .card--back .brand {
    position: absolute;
    top: 70px; left: 0; right: 0;
    justify-content: center;
  }
  .services {
    position: absolute;
    top: 150px; left: 0; right: 0;
    text-align: center;
    color: var(--text-grey);
    font-size: 15px;
    line-height: 27px;
  }
  .services .sep { color: var(--brand-blue); padding: 0 6px; }

  .card--front .brand {
    position: absolute;
    top: 40px; left: 34px;
    font-size: 22px;
  }
  .swoosh { position: absolute; inset: 0; }
  .holder {
    position: absolute;
    right: 34px; top: 108px;
    text-align: right;
  }
  .holder__name {
    color: var(--brand-blue);
    font-weight: 700;
    font-style: italic;
    font-size: 20px;
  }
  .holder__role {
    color: var(--text-grey);
    font-size: 14px;
    margin-top: 2px;
  }
  .contact {
    position: absolute;
    right: 34px; top: 214px;
    text-align: right;
    color: var(--on-blue);
    font-size: 14px;
    line-height: 19px;
    list-style: none;
  }
  .contact__address { margin-bottom: 6px; }
  .contact__row {
    display: flex;
    justify-content: flex-end;
    align-items: center;
    gap: 8px;
  }
  .contact__row svg { width: 14px; height: 14px; flex: none; }
</style>
</head>
<body>

<section class="card card--back" aria-label="Card back – services">
  <div class="brand"><span class="brand__dot"></span>Bluefern Roving Sonography</div>
  <div class="services">
    <p>Abdomen (AB)<span class="sep">•</span>Vascular Technology (VT)<span class="sep">•</span>Breast (BR)</p>
    <p>Pediatric Sonography (PS)<span class="sep">•</span>Fetal Echocardiography (FE)</p>
    <p>Adult Echocardiography (AE)<span class="sep">•</span>Pediatric Echocardiography (PE)</p>
    <p>Musculoskeletal Sonography (MSK)<span class="sep">•</span>Obstetrics and Gynecology (OB/GYN)</p>
  </div>
</section>

<section class="card card--front" aria-label="Card front – contact">
  <svg class="swoosh" viewBox="0 0 630 360" preserveAspectRatio="none" aria-hidden="true">
    <defs>
      <linearGradient id="blueFill" x1="0" y1="0" x2="1" y2="1">
        <stop offset="0" stop-color="#1479a8"/>
        <stop offset="0.45" stop-color="#35b0de"/>
        <stop offset="1" stop-color="#0f5f88"/>
      </linearGradient>
    </defs>
    <path d="M0,112 C120,146 260,172 630,174 L630,190 C300,192 130,168 0,146 Z" fill="var(--band-grey)"/>
    <path d="M0,158 C140,192 300,200 630,194 L630,360 L0,360 Z" fill="url(#blueFill)"/>
    <path d="M40,172 C180,202 360,206 630,200" fill="none" stroke="#ffffff" stroke-width="3"/>
  </svg>

  <div class="brand"><span class="brand__dot"></span>Bluefern Roving Sonography</div>

  <div class="holder">
    <p class="holder__name">Dana Whitlock</p>
    <p class="holder__role">President</p>
  </div>

  <ul class="contact">
    <li class="contact__address">4072 Heron Crest Blvd<br>#218, Royal Palm Beach<br>Florida 33411</li>
    <li class="contact__row">561-555-0147
      <svg viewBox="0 0 24 24"><path fill="#fff" d="M6.6 10.8a15 15 0 0 0 6.6 6.6l2.2-2.2a1 1 0 0 1 1-.25 11.4 11.4 0 0 0 3.6.57 1 1 0 0 1 1 1V20a1 1 0 0 1-1 1A17 17 0 0 1 3 4a1 1 0 0 1 1-1h3.5a1 1 0 0 1 1 1c0 1.25.2 2.45.57 3.57a1 1 0 0 1-.25 1z"/></svg>
    </li>
    <li class="contact__row">bluefern.roving.bs@kelvamail.net
      <svg viewBox="0 0 24 24"><rect x="2" y="5" width="20" height="14" rx="1" fill="#fff"/><path d="M3 6l9 7 9-7" fill="none" stroke="#1479a8" stroke-width="1.8"/></svg>
    </li>
    <li class="contact__row">bluefernrovingsonography.com
      <svg viewBox="0 0 24 24"><circle cx="12" cy="12" r="9.5" fill="none" stroke="#fff" stroke-width="2"/><path d="M2.5 12h19M12 2.5c3 3 3 16 0 19M12 2.5c-3 3-3 16 0 19" fill="none" stroke="#fff" stroke-width="1.6"/></svg>
    </li>
  </ul>
</section>

</body>
</html>
```